Fern Trader Supply Banners

We are looking for web banners that describe our business, we are an online shopping portal for businesses to buy natural and organic products direct form the manufacturers of those products.

1. Homepage banners (you can do 1 banner or up to 4 scrolling banners that describe the business. Width 780 * Height 235

This is where the hompage banner or banners will go.
http://www.ferntradersupply.example/

2. Banners to use on other websites 3 banners 250 x 250 120 x 300 300 x 90

Target Market(s)

The retail world, off the natural and organic product word, vegans, Gluten free, ext.

Industry/Entity Type

Online Shopping

Requirements
Must have
• Must match our site and tell our message well.

```html
<!DOCTYPE html>
<html lang="en">
<head>
<meta charset="utf-8">
<title>Fern Trader Supply – Find Nature In Everything You Use</title>
<link rel="stylesheet" href="https://fonts.googleapis.com/css2?family=Share+Tech+Mono&display=swap">
<style>
  :root {
    --paper: #ffffff;
    --bar: #000000;
    --orange: #f9a94b;
    --leaf: #6db843;
    --leaf-text: #6ab04c;
    --outline: #3b3b3b;
    --label: #ffffff;
  }
  html, body {
    margin: 0;
    padding: 0;
    width: 1200px;
    height: 362px;
    overflow: hidden;
    background: var(--paper);
  }
  .banner {
    position: relative;
    width: 1200px;
    height: 362px;
    font-family: "Share Tech Mono", monospace;
  }
  .masthead {
    position: absolute;
    inset: 0 0 auto 0;
    height: 74px;
    background: var(--paper);
  }
  .brand {
    position: absolute;
    left: 16px;
    top: 22px;
    display: flex;
    align-items: center;
    gap: 8px;
    margin: 0;
    font-size: 17px;
    font-weight: 400;
    color: var(--leaf-text);
    white-space: nowrap;
  }
  .brand-dot {
    width: 16px;
    height: 16px;
    border-radius: 50%;
    background: var(--leaf);
  }
  .tagline {
    position: absolute;
    left: 280px;
    top: 14px;
    margin: 0;
    font-size: 35px;
    font-weight: 400;
    color: var(--leaf-text);
    letter-spacing: 0.5px;
    white-space: nowrap;
  }
  .rail {
    position: absolute;
    left: 0;
    top: 74px;
    width: 1200px;
    height: 18px;
    background: var(--bar);
  }
  .categories {
    position: absolute;
    left: 0;
    top: 92px;
    width: 1200px;
    height: 270px;
    background: var(--orange);
  }
  .categories svg { display: block; }
  .cord { stroke: var(--outline); stroke-width: 1.5; }
  .bubble { fill: var(--leaf); stroke: var(--outline); stroke-width: 1.5; }
  .label {
    fill: var(--label);
    font-family: "Share Tech Mono", monospace;
    font-size: 12px;
    text-anchor: middle;
    letter-spacing: 0.3px;
  }
</style>
</head>
<body>
<div class="banner">
  <header class="masthead">
    <p class="brand"><span class="brand-dot"></span>Fern Trader Supply</p>
    <h1 class="tagline">Find Nature In Everything You Use</h1>
  </header>
  <div class="rail"></div>
  <nav class="categories" aria-label="Product categories">
    <svg width="1200" height="270" viewBox="0 0 1200 270">
      <!-- upper row -->
      <g class="category">
        <line class="cord" x1="131" y1="0" x2="131" y2="8"/>
        <circle class="bubble" cx="131" cy="62" r="54"/>
        <text class="label" x="131" y="59">APPAREL/</text>
        <text class="label" x="131" y="75">ACCESSORIES</text>
      </g>
      <g class="category">
        <line class="cord" x1="320" y1="0" x2="320" y2="8"/>
        <circle class="bubble" cx="320" cy="62" r="54"/>
        <text class="label" x="320" y="67">BEVERAGES</text>
      </g>
      <g class="category">
        <line class="cord" x1="515" y1="0" x2="515" y2="8"/>
        <circle class="bubble" cx="515" cy="62" r="54"/>
        <text class="label" x="515" y="67">BULK</text>
      </g>
      <g class="category">
        <line class="cord" x1="708" y1="0" x2="708" y2="8"/>
        <circle class="bubble" cx="708" cy="62" r="54"/>
        <text class="label" x="708" y="59">FRESH</text>
        <text class="label" x="708" y="75">FOOD</text>
      </g>
      <g class="category">
        <line class="cord" x1="897" y1="0" x2="897" y2="8"/>
        <circle class="bubble" cx="897" cy="62" r="54"/>
        <text class="label" x="897" y="67">GROCERY</text>
      </g>
      <g class="category">
        <line class="cord" x1="1088" y1="0" x2="1088" y2="8"/>
        <circle class="bubble" cx="1088" cy="62" r="54"/>
        <text class="label" x="1088" y="67">HOUSEHOLD</text>
      </g>
      <!-- lower row -->
      <g class="category">
        <line class="cord" x1="234" y1="0" x2="234" y2="142"/>
        <circle class="bubble" cx="234" cy="196" r="54"/>
        <text class="label" x="234" y="201">BATH/BODY</text>
      </g>
      <g class="category">
        <line class="cord" x1="420" y1="0" x2="420" y2="142"/>
        <circle class="bubble" cx="420" cy="196" r="54"/>
        <text class="label" x="420" y="201">BOOKS</text>
      </g>
      <g class="category">
        <line class="cord" x1="615" y1="0" x2="615" y2="142"/>
        <circle class="bubble" cx="615" cy="196" r="54"/>
        <text class="label" x="615" y="201">SNACKS</text>
      </g>
      <g class="category">
        <line class="cord" x1="795" y1="0" x2="795" y2="142"/>
        <circle class="bubble" cx="795" cy="196" r="54"/>
        <text class="label" x="795" y="201">FROZEN</text>
      </g>
      <g class="category">
        <line class="cord" x1="982" y1="0" x2="982" y2="142"/>
        <circle class="bubble" cx="982" cy="196" r="54"/>
        <text class="label" x="982" y="201">HERBS</text>
      </g>
    </svg>
  </nav>
</div>
</body>
</html>
```